Veterinary hospital brochure design

we need brochure design for our veterinary hospital, something interesting, catchy and unique. Once we get going we need to add few unique services we offer and should be highlighted.Nice colors, and should be very professional looking. Brochure to be tri fold, nice colors highlight our services.
Like shades of blues or green.This is full service veterinary hospital. We do focus and specialize in Canine reproduction.

Target Market(s)

pet owners

Industry/Entity Type

Hospital

Font styles to use
Serif
Script

Requirements
Must have
• catchy words
• unique design
• have our unique services included
Nice to have
• good pictures and catchy words etc etc

```html
<!DOCTYPE html>
<html lang="en">
<head>
<meta charset="utf-8">
<title>Willowmere Hospital for Animals – Tri-fold Brochure</title>
<link href="https://fonts.googleapis.com/css2?family=Open+Sans:wght@300;400;600;700;800&display=swap" rel="stylesheet">
<style>
  :root{
    --red:#b01f2e;
    --red-dark:#931826;
    --green:#5ea52f;
    --teal:#11a08a;
    --white:#ffffff;
    --paper:#f6f6f4;
    --ink:#2a2a2a;
    --band:#e4e4e4;
    --social:#1f4f8f;
  }
  *{margin:0;padding:0;box-sizing:border-box}
  html,body{width:1200px;height:800px;overflow:hidden;background:#3a3a3a}
  body{font-family:"Open Sans",Arial,sans-serif;color:var(--ink)}
  .brochure{position:relative;width:1200px;height:800px;background:var(--paper);overflow:hidden}
  .shapes{position:absolute;inset:0}
  .fold{position:absolute;top:0;bottom:0;width:1px;background:rgba(0,0,0,.08)}
  .fold--one{left:400px}.fold--two{left:800px}

  .intro-text{position:absolute;left:36px;top:88px;width:300px;font-size:14px;line-height:1.5;color:#333}
  .photo{position:absolute;border-radius:50%;border:9px solid var(--green);overflow:hidden}
  .photo--kitten{left:100px;top:420px;width:220px;height:220px;background:radial-gradient(circle at 55% 40%,#ffffff 0 30%,#dcdde2 55%,#b9a89b 100%)}
  .closing-text{position:absolute;left:192px;top:654px;width:196px;font-size:13px;line-height:1.45;color:var(--white);text-align:center}

  .services{position:absolute;left:440px;top:56px;list-style:none;color:var(--white);font-size:14px;line-height:1.55}
  .services li{display:flex;align-items:center;gap:10px}
  .services li::before{content:"";width:8px;height:8px;border-radius:50%;background:var(--white);flex:none}
  .doctor{position:absolute;left:440px;top:330px;color:var(--white)}
  .doctor__name{font-size:19px;font-weight:300}
  .doctor__focus{margin-top:8px;font-size:19px;font-weight:700;line-height:1.35}
  .address{position:absolute;left:470px;top:478px;display:flex;gap:10px;color:var(--white);font-size:13px;line-height:1.4}
  .map{position:absolute;left:610px;top:500px;width:230px;height:230px;border-radius:50%;border:9px solid var(--green);background:radial-gradient(circle,#eef0e6 0,#dfe4d3 70%,#cdd6c0 100%);display:flex;align-items:center;justify-content:center}
  .map__label{font-size:24px;font-weight:600;color:#222;text-align:center;line-height:1.2}
  .social{position:absolute;left:540px;top:750px;display:flex;gap:12px}
  .social span{width:22px;height:22px;border-radius:50%;background:var(--social)}

  .headline{position:absolute;left:840px;top:34px;color:#111;line-height:1.05}
  .headline__lead,.headline__close{font-size:36px;font-weight:800}
  .headline__love{font-size:36px;font-weight:300}
  .headline__care{font-size:20px;font-weight:700}
  .photo--vet{left:850px;top:250px;width:340px;height:300px;border:none;border-radius:0 0 0 140px;background:linear-gradient(135deg,#f3f4f6 0%,#e9e2d6 45%,#d8c7a8 70%,#c9d3df 100%)}
  .brand{position:absolute;left:850px;top:604px;display:flex;align-items:center;gap:10px;font-size:18px;font-weight:400;color:#444;white-space:nowrap}
  .brand__mark{width:32px;height:32px;border-radius:50%;border:2px solid #444;flex:none}
  .phone{position:absolute;left:880px;top:722px;display:flex;align-items:center;gap:12px;color:var(--white);font-size:28px;font-weight:700}
</style>
</head>
<body>
<main class="brochure">
  <svg class="shapes" width="1200" height="800" viewBox="0 0 1200 800" aria-hidden="true">
    <defs>
      <clipPath id="right-side"><rect x="600" y="0" width="600" height="800"/></clipPath>
      <path id="red-wave" d="M372 0 L770 0 C860 120 860 300 800 420 C760 500 740 580 760 800 L150 800 C120 740 125 680 170 640 C260 570 350 510 392 420 C415 340 410 200 372 0 Z"/>
    </defs>
    <rect x="800" y="0" width="400" height="800" fill="#fbfbfb"/>
    <path d="M800 560 L1200 470 L1200 690 L800 690 Z" fill="var(--band)"/>
    <path d="M800 690 L1200 640 L1200 800 L800 800 Z" fill="var(--green)"/>
    <use href="#red-wave" transform="translate(18 0)" fill="var(--teal)" clip-path="url(#right-side)"/>
    <use href="#red-wave" transform="translate(-16 0)" fill="var(--green)"/>
    <use href="#red-wave" fill="var(--red)"/>
  </svg>
  <div class="fold fold--one"></div>
  <div class="fold fold--two"></div>

  <p class="intro-text">Lorem ipsum dolor sit amet, consectetur adipiscing elit, sed do eiusmod tempor incididunt ut labore et dolore magna aliqua. Ut enim ad minim veniam, quis nostrud exercitation ullamco laboris nisi ut aliquip ex ea commodo consequat. Duis aute irure dolor in reprehenderit in voluptate velit esse cillum dolore eu fugiat nulla pariatur. Excepteur sint occaecat cupidatat non proident, sunt in culpa qui officia deserunt mollit anim id est laborum."</p>
  <div class="photo photo--kitten" role="img" aria-label="Photo of a white kitten being checked with a stethoscope"></div>
  <p class="closing-text">Lorem ipsum dolor sit amet, consectetur adipiscing elit, sed do eiusmod tempor incididunt ut labore et dolore magna aliqua. Ut enim ad minim veniam, quis nostrud</p>

  <ul class="services">
    <li>Breeding Soundness Exams</li>
    <li>Semen Collection</li>
    <li>Computer Assisted Semen Analysis</li>
    <li>Caesarian Sections</li>
    <li>Ovulation Timing</li>
    <li>Infertility Work-Ups</li>
    <li>Transcervical Insemination</li>
    <li>Surgical Insemination</li>
    <li>Pregnancy Ultrasound</li>
    <li>Semen Freezing</li>
  </ul>
  <div class="doctor">
    <p class="doctor__name">Dr. Maren Okafor, DVM</p>
    <p class="doctor__focus">Expertise in<br>Canine Reproduction<br>and Infertility</p>
  </div>
  <div class="address">
    <svg width="14" height="20" viewBox="0 0 14 20" aria-hidden="true"><circle cx="7" cy="7" r="5" fill="none" stroke="#fff" stroke-width="2"/><path d="M7 12 V18 M2 18 H12" stroke="#fff" stroke-width="2"/></svg>
    <p>Address Line 1<br>Address Line 2</p>
  </div>
  <div class="map" role="img" aria-label="Street map showing the hospital location">
    <p class="map__label">Your address<br>map here</p>
  </div>
  <div class="social" aria-label="Social media links"><span></span><span></span><span></span></div>

  <h1 class="headline">
    <span class="headline__lead">Got Pets?</span><br>
    <span class="headline__love">We Love</span><br>
    <span class="headline__care">&amp; Care</span><br>
    <span class="headline__close">For Them!</span>
  </h1>
  <div class="photo photo--vet" role="img" aria-label="Photo of a smiling veterinarian hugging a golden retriever"></div>
  <div class="brand"><span class="brand__mark"></span>Willowmere Hospital for Animals</div>
  <div class="phone">
    <svg width="28" height="28" viewBox="0 0 28 28" aria-hidden="true"><circle cx="14" cy="14" r="12" fill="none" stroke="#fff" stroke-width="2"/><path d="M10 8 L12 8 L13 11 L11.5 12.5 C12.5 14.5 13.5 15.5 15.5 16.5 L17 15 L20 16 L20 18 C20 19 19 20 18 20 C12.5 19.5 8.5 15.5 8 10 C8 9 9 8 10 8 Z" fill="#fff"/></svg>
    (555) 014-2290
  </div>
</main>
</body>
</html>
```